A3 Menus for new international restaurant in Singapore.

Looking for new A3 menu design for indoor & outdoor (beautiful garden and trees) restaurant that caters for expat and local families. International menu, cool jazz vibe, great for couples and families. Restaurant called Brass Cove Parlour. I have attached some of the logos we use. Will consider black and white or color options. Restaurant located on a hill where there were tin mines many years ago, hence the name and branding. Looking for three menus (1) Dinner (2) Lunch (3) weekend brunch.

Target Market(s)

Families, young couples and professionals.

Industry/Entity Type

Restaurant

Font styles to use
Serif
Sans Serif

Requirements
Must have
• All food layout on one side of A3, one for each attached menu. Also a space for drinks list on the back.
Nice to have
• Use some of the logo material we have attached.
Should not have

```html
<!DOCTYPE html>
<html lang="en">
<head>
<meta charset="utf-8">
<title>Brass Cove Parlour – Main Courses</title>
<link href="https://fonts.googleapis.com/css2?family=Lato:wght@400&family=Cormorant+Garamond:wght@400;500&display=swap" rel="stylesheet">
<style>
  :root {
    --paper: #ffffff;
    --ink: #1e1e1e;
    --accent-red: #c8202f;
    --footer-grey: #6a6a6a;
    --art-dark: #1a1a1a;
    --art-mid: #4a4a4a;
  }
  * { margin: 0; padding: 0; box-sizing: border-box; }
  html, body { width: 848px; height: 1200px; overflow: hidden; background: var(--paper); }
  .menu-page {
    position: relative;
    width: 848px;
    height: 1200px;
    background: var(--paper);
    color: var(--ink);
    font-family: "Lato", sans-serif;
    font-size: 9.6px;
    line-height: 17.5px;
  }
  .menu-column { position: absolute; top: 165px; }
  .menu-column--left { left: 143px; width: 235px; }
  .menu-column--right { left: 487px; width: 230px; }
  .dish { margin-bottom: 35px; }
  .dish--pasta { margin-bottom: 17.5px; }
  .section-title {
    position: absolute;
    left: 403px;
    top: 165px;
    writing-mode: vertical-rl;
    font-family: "Cormorant Garamond", serif;
    font-weight: 400;
    font-size: 34px;
    letter-spacing: 1px;
    line-height: 1;
    color: var(--accent-red);
  }
  .tree-art {
    position: absolute;
    background: linear-gradient(180deg, var(--art-dark), var(--art-mid));
    border-radius: 30px 30px 2px 2px;
  }
  .tree-art--single { left: 430px; top: 75px; width: 60px; height: 90px; }
  .tree-art--cluster { left: 632px; top: 0; width: 216px; height: 165px; border-radius: 0 0 2px 60px; }
  .price-note {
    position: absolute;
    left: 370px;
    top: 1133px;
    font-family: "Cormorant Garamond", serif;
    font-variant: small-caps;
    font-size: 10.5px;
    letter-spacing: 0.3px;
    color: var(--footer-grey);
    white-space: nowrap;
  }
  .brand-mark {
    position: absolute;
    left: 728px;
    top: 1095px;
    width: 90px;
    display: flex;
    flex-direction: column;
    align-items: center;
    gap: 5px;
    font-family: "Lato", sans-serif;
    font-size: 9px;
    line-height: 11px;
    text-align: center;
    color: var(--ink);
  }
  .brand-mark__dot { width: 26px; height: 26px; border: 1px solid var(--ink); border-radius: 50%; }
</style>
</head>
<body>
<main class="menu-page">
  <div class="tree-art tree-art--single" role="img" aria-label="Illustration of a round tree with a key motif"></div>
  <div class="tree-art tree-art--cluster" role="img" aria-label="Illustration of a cluster of round trees with key motifs"></div>

  <section class="menu-column menu-column--left">
    <p class="dish">Brass Cove Parlour Burger<br>200gms ground prime beef served in a homemade<br>brioche bun with lettuce, tomato and mayo<br>served with a side of fries<br>$22<br>top it with cheese or bacon or both – add $2 for<br>each</p>
    <p class="dish">Brass Cove Parlour Bangers &amp; Mash<br>prime pork sausages, buttery mashed potato covered<br>in onion &amp; cider gravy<br>$22</p>
    <p class="dish">Hay Smoked Pork Ribs<br>home-smoked, slow-cooked ribs, served with spicy<br>chimichurri sauce and fries<br>$26</p>
    <p class="dish">Pan Seared Black Cod<br>served on a bed of vermicelli, lemongrass, fresh chilli<br>and kaffir lime leaves<br>$35</p>
    <p class="dish">Beef Tenderloin<br>200gms grilled to your choice, served with roasted<br>vine tomatoes and red wine gravy,<br>accompanied by buttery mashed potato or fries<br>$35</p>
    <p class="dish">Roast Chicken<br>share a whole bird for 2, with jus and your choice of<br>two sides. (Allow 25 mins to prepare)<br>$38</p>
  </section>

  <h1 class="section-title">MAIN COURSES</h1>

  <section class="menu-column menu-column--right">
    <p class="dish">Brass Cove Parlour's Seafood Stew<br>classic seafood stew, served in the pan with fresh<br>black cod, prawns, calamari, clams and mussels,<br>cookedin a prawn bisque, with bread for dipping<br>$30</p>
    <p class="dish">Roast Pork Belly<br>served with apple compote and your choice of two<br>sides. Whole belly shared among 3-4 people.<br>(Allow 45 mins to roast.)<br>$85</p>
    <p class="dish">Beef T-Bone<br>600gms T-Bone grilled, served with red wine gravy<br>and your choice of two sides (Shared among 2<br>people. Allow 25 mins to cook)<br>$70</p>
    <p class="dish dish--pasta">Strigoli- &nbsp;with beef ragubolognese$22</p>
    <p class="dish dish--pasta">Linguini- with a light creamy carbonara sauce, with<br>smoked pancetta$23</p>
    <p class="dish dish--pasta">Rigatoni - with aglio, olio and pepperoncino$20,with<br>prawns, add$5</p>
    <p class="dish dish--pasta">Risotto - with rich porcini mushrooms and crutin<br>cheese$22</p>
  </section>

  <p class="price-note">All prices are in Singapore dollars and are subject to GST &amp; 10% service charge</p>

  <div class="brand-mark">
    <span class="brand-mark__dot"></span>
    <span>Brass Cove Parlour</span>
  </div>
</main>
</body>
</html>
```